Horse Brush Package design -

I need a design for a box - required for a rubber horse brush used for grooming and removing excess hair. The Brand is 'Maple Ridge Equestrian' and we develop top quality horse products. The design should be classy and professional

Box size is 21.5cm Length * 2cm high * 5 cm wide
Photo of logo and brush attached.
Box needs to have logo and description on front
Barcode on back.
Additional designs and photos can be added as you see fit.

"Horse Deshedding & Grooming Brush"
Brush away excess coat and dander
Gently remove dirt and mud
Soft, flexible design to gently groom around legs, ears and face.
Used when washing gives a deep clean to remove dirt
Gentle massage for increasing circulation
Durable, gentle, and kind to the horse

Target Market(s)

Horse Owners

Requirements
Must have
• Logo on the front, space for barcode on the back
Nice to have
• A nice horse photo would be suitable

```html
<!DOCTYPE html>
<html lang="en">
<head>
<meta charset="utf-8">
<title>Maple Ridge Equestrian – Grooming Brush Box</title>
<link href="https://fonts.googleapis.com/css2?family=Bree+Serif&family=Roboto+Condensed:wght@400;500&display=swap" rel="stylesheet">
<style>
  :root {
    --bg: #86878b;
    --ink: #3b3b3d;
    --paper: #ffffff;
    --gold-dark: #c48f2c;
    --gold-light: #f3d479;
    --line: #1d1d1f;
    --headline: #2c2c2e;
  }
  html, body {
    margin: 0;
    width: 1200px;
    height: 800px;
    overflow: hidden;
    background: var(--bg);
  }
  .stage {
    width: 1200px;
    height: 800px;
    display: flex;
    align-items: center;
    justify-content: center;
  }
  .dieline { display: block; }
  .flap { fill: var(--ink); stroke: var(--line); stroke-width: 1.5; }
  .fold { stroke: var(--line); stroke-width: 1.5; fill: none; }
  .side-panel { fill: url(#gold); }
  .face-panel { fill: var(--paper); }
  .footer-band { fill: var(--ink); }
  .footer-rule { fill: none; stroke: var(--gold-dark); stroke-width: 3; }
  .brand-name { font-family: "Bree Serif", serif; font-size: 14px; fill: var(--gold-dark); }
  .brand-sub { font-family: "Bree Serif", serif; font-size: 9px; fill: var(--gold-dark); }
  .title { font-family: "Bree Serif", serif; fill: var(--headline); font-size: 23px; }
  .title-big { font-family: "Bree Serif", serif; fill: var(--headline); font-size: 40px; }
  .side-title { font-family: "Bree Serif", serif; fill: var(--headline); font-size: 22px; }
  .tagline { font-family: "Roboto Condensed", sans-serif; font-weight: 500; fill: var(--paper); font-size: 18px; }
  .small-copy { font-family: "Roboto Condensed", sans-serif; fill: var(--paper); font-size: 9.5px; }
  .barcode-box { fill: var(--paper); }
  .barcode-label { font-family: "Roboto Condensed", sans-serif; font-weight: 500; fill: var(--headline); font-size: 19px; }
</style>
</head>
<body>
<main class="stage">
  <svg class="dieline" width="345" height="780" viewBox="1080 40 490 1120" xmlns="http://www.w3.org/2000/svg">
    <defs>
      <linearGradient id="gold" x1="0" y1="0" x2="1" y2="0">
        <stop offset="0" stop-color="var(--gold-dark)"/>
        <stop offset="0.55" stop-color="var(--gold-light)"/>
        <stop offset="1" stop-color="var(--gold-dark)"/>
      </linearGradient>
      <linearGradient id="brushTone" x1="0" y1="0" x2="1" y2="1">
        <stop offset="0" stop-color="#2a2a2c"/>
        <stop offset="1" stop-color="#5a5a5e"/>
      </linearGradient>
      <linearGradient id="horseTone" x1="0" y1="0" x2="0" y2="1">
        <stop offset="0" stop-color="#2b1f22"/>
        <stop offset="1" stop-color="#120e10"/>
      </linearGradient>
    </defs>

    <!-- top flaps -->
    <path class="flap top-tuck" d="M1153 268 V70 Q1153 48 1175 48 H1289 Q1311 48 1311 70 V268 Z"/>
    <line class="fold" x1="1153" y1="110" x2="1311" y2="110"/>
    <path class="flap dust-flap" d="M1090 268 V203 H1124 L1153 240 V268 Z"/>
    <path class="flap dust-flap" d="M1311 268 V235 H1340 L1370 258 V268 Z"/>

    <!-- bottom flaps -->
    <path class="flap bottom-tuck" d="M1373 930 V1128 Q1373 1150 1395 1150 H1509 Q1531 1150 1531 1128 V930 Z"/>
    <line class="fold" x1="1373" y1="1088" x2="1531" y2="1088"/>
    <path class="flap dust-flap" d="M1090 930 V965 H1124 L1153 940 V930 Z"/>
    <path class="flap dust-flap" d="M1311 930 L1320 997 H1370 V930 Z"/>

    <!-- side panels -->
    <rect class="side-panel" x="1090" y="268" width="63" height="662"/>
    <rect class="side-panel" x="1311" y="268" width="62" height="662"/>
    <rect class="side-panel" x="1531" y="268" width="31" height="662"/>
    <text class="side-title" transform="translate(1129 600) rotate(-90)" text-anchor="middle" textLength="414" lengthAdjust="spacingAndGlyphs">Horse Deshedding &amp; Grooming Brush</text>
    <text class="side-title" transform="translate(1349 600) rotate(-90)" text-anchor="middle" textLength="414" lengthAdjust="spacingAndGlyphs">Horse Deshedding &amp; Grooming Brush</text>

    <!-- front panel -->
    <g class="front-panel">
      <rect class="face-panel" x="1153" y="268" width="158" height="662"/>
      <text class="brand-name" x="1165" y="318">MAPLE RIDGE</text>
      <text class="brand-sub" x="1165" y="330">EQUESTRIAN</text>
      <text class="title" x="1164" y="377">Horse</text>
      <text class="title" x="1164" y="401" textLength="132" lengthAdjust="spacingAndGlyphs">Deshedding</text>
      <text class="title" x="1164" y="424" textLength="132" lengthAdjust="spacingAndGlyphs">&amp; Grooming</text>
      <text class="title-big" x="1164" y="460" textLength="134" lengthAdjust="spacingAndGlyphs">BRUSH</text>
      <rect role="img" aria-label="Photo of the black rubber grooming brush" x="1172" y="472" width="130" height="90" rx="10" fill="url(#brushTone)"/>
      <rect role="img" aria-label="Photo of a galloping black horse" x="1160" y="568" width="145" height="180" rx="6" fill="url(#horseTone)"/>
      <path class="footer-band" d="M1153 770 Q1232 735 1311 770 V930 H1153 Z"/>
      <path class="footer-rule" d="M1153 770 Q1232 735 1311 770"/>
      <text class="tagline" text-anchor="middle" x="1230" y="785">Brush</text>
      <text class="tagline" text-anchor="middle" x="1230" y="807">Away Excess</text>
      <text class="tagline" text-anchor="middle" x="1230" y="829">Coat and Dander</text>
      <text class="small-copy" text-anchor="middle" x="1231" y="867">Gently remove dirt and mud Soft,</text>
      <text class="small-copy" text-anchor="middle" x="1231" y="881">flexible design to gently groom</text>
      <text class="small-copy" text-anchor="middle" x="1231" y="895">around legs, ears and face.</text>
    </g>

    <!-- back panel -->
    <g class="back-panel">
      <rect class="face-panel" x="1373" y="268" width="158" height="662"/>
      <text class="brand-name" x="1385" y="318">MAPLE RIDGE</text>
      <text class="brand-sub" x="1385" y="330">EQUESTRIAN</text>
      <text class="title" x="1384" y="377">Horse</text>
      <text class="title" x="1384" y="401" textLength="132" lengthAdjust="spacingAndGlyphs">Deshedding</text>
      <text class="title" x="1384" y="424" textLength="132" lengthAdjust="spacingAndGlyphs">&amp; Grooming</text>
      <text class="title-big" x="1384" y="460" textLength="134" lengthAdjust="spacingAndGlyphs">BRUSH</text>
      <rect role="img" aria-label="Photo of the black rubber grooming brush" x="1392" y="472" width="130" height="90" rx="10" fill="url(#brushTone)"/>
      <rect role="img" aria-label="Photo of a galloping black horse" x="1380" y="568" width="145" height="180" rx="6" fill="url(#horseTone)"/>
      <path class="footer-band" d="M1373 770 Q1452 735 1531 770 V930 H1373 Z"/>
      <path class="footer-rule" d="M1373 770 Q1452 735 1531 770"/>
      <text class="small-copy" text-anchor="middle" x="1452" y="776">Used when</text>
      <text class="small-copy" text-anchor="middle" x="1452" y="790">washing gives a deep clean to</text>
      <text class="small-copy" text-anchor="middle" x="1452" y="804">remove dirt Gentle massage for</text>
      <text class="small-copy" text-anchor="middle" x="1452" y="818">increasing circulation Durable,</text>
      <text class="small-copy" text-anchor="middle" x="1452" y="832">gentle, and kind to the horse</text>
      <rect class="barcode-box" x="1385" y="851" width="134" height="71"/>
      <text class="barcode-label" text-anchor="middle" x="1452" y="893">bar code</text>
    </g>
  </svg>
</main>
</body>
</html>
```